Stationary Set Rebrand for Brenvik

We are a Canadian Distribution and Service Company that was established in 1969. Over the past 5 decades we have expanded our business and have warehouses across Canada. We specialize in adhesive tapes, adhesives, films, safety, warehouse, shipping, janitorial and packaging supplies.

We have updated our logo design and would like a new corporate branding identity that includes a new fresh Stationary Set (Business Cards, Letterhead, Letterhead MS Word, Envelope, Presentation Folders, Email Signatures, Notepad Covers, etc.)

Target Market(s)

Industrial Business Sector

Font styles to use
Sans Serif

Colors
0054AA
0677BA
7BADD7
CADEEF
E8F1F8
0094D4
00A9DD
6FCCEA
C7EBF8
E9F6FB
00AB8E
00BBA5
67D7C9
C6EFE9
E9F9F6
EB3D1F
EC4F4E
F09395
F8D3D4
FCEDEE

Requirements
Should not have
• Colors not too light, darker colours preferred

```html
<!DOCTYPE html>
<html lang="en">
<head>
<meta charset="utf-8">
<title>Brenvik Stationery Set</title>
<link rel="stylesheet" href="https://fonts.googleapis.com/css2?family=Archivo:wght@400;500;700;800&display=swap">
<style>
:root{
  --red:#d7191f;
  --ink:#231f20;
  --paper:#f6f1f2;
  --white:#ffffff;
  --stage:#3a3a3b;
  --grey:#555;
  --rule:#c9c4c5;
}
*{box-sizing:border-box;margin:0;padding:0}
html,body{width:1200px;height:933px;overflow:hidden}
body{background:var(--stage);font-family:"Archivo",sans-serif;position:relative;color:var(--ink)}
.piece{position:absolute;overflow:hidden;box-shadow:0 3px 10px rgba(0,0,0,.35)}
.brand{font-weight:800;letter-spacing:-.02em;line-height:1;white-space:nowrap}
.brand-tag{font-weight:500;line-height:1;white-space:nowrap;display:block}
.brand--light{color:var(--white)}
.brand--dark{color:var(--ink)}
.contact{list-style:none;font-size:5.2px;line-height:1.25;letter-spacing:.03em}
.contact li{display:flex;align-items:center;gap:3px}
.icon{width:5px;height:5px;flex:none}
.icon--red{fill:var(--red)}
.icon--white{fill:var(--white)}

/* business card front */
.card-front{left:38px;top:102px;width:219px;height:125px;background:var(--white);border-radius:6px}
.card-front .lockup{position:absolute;left:27px;top:47px}
.card-front .brand{font-size:21px}
.card-front .brand-tag{font-size:4px;margin-top:1px}
.card-front .divider{position:absolute;left:117px;top:26px;width:1px;height:73px;background:var(--rule)}
.card-front .holder{position:absolute;left:125px;top:28px}
.holder-name{font-weight:800;color:var(--red);font-size:8px;letter-spacing:.04em}
.holder-role{font-size:5px;color:var(--grey);margin-top:2px}
.card-front .address{font-size:5.2px;line-height:1.3;margin-top:6px;letter-spacing:.03em}
.card-front .contact{margin-top:4px}

/* business card back */
.card-back{left:34px;top:275px;width:223px;height:128px;background:var(--red);border-radius:6px}
.card-back .mark{position:absolute;left:101px;top:42px;width:22px;height:22px;background:var(--white);border-radius:50%}
.card-back .web{position:absolute;left:0;right:0;top:111px;text-align:center;color:var(--white);font-size:5.5px;font-weight:500}

/* letterhead */
.letterhead{left:280px;top:45px;width:306px;height:431px;background:var(--paper)}
.letterhead .header{height:54px;background:var(--red);position:relative;color:var(--white)}
.letterhead .header .lockup{position:absolute;left:31px;top:18px}
.letterhead .brand{font-size:19px}
.letterhead .brand-tag{font-size:3.8px;margin-top:1px}
.letterhead .header-address{position:absolute;right:83px;top:21px;text-align:right;font-size:5px;line-height:1.3;letter-spacing:.03em}
.letterhead .header-rule{position:absolute;left:227px;top:20px;width:1px;height:18px;background:var(--white)}
.letterhead .header .contact{position:absolute;left:231px;top:20px;font-size:5px;line-height:1.3}
.letter-body{padding:50px 29px 0 31px;color:var(--grey)}
.salutation{font-size:8.5px;margin-bottom:14px}
.letter-body p{font-size:4.4px;line-height:1.65;text-align:justify;margin-bottom:6px}
.signoff{font-size:4.6px;margin-top:12px}
.signature-line{width:40px;height:1px;background:var(--ink);margin:10px 0 12px}
.signer{font-size:6.5px}
.signer-role{font-size:5px;margin-top:2px}

/* envelope strip */
.env-strip{left:632px;top:80px;width:312px;height:85px;background:var(--paper)}
.env-strip .header{height:40px;background:var(--red);position:relative}
.env-strip .lockup{position:absolute;left:17px;top:10px}
.env-strip .brand{font-size:19px}
.env-strip .brand-tag{font-size:3.8px;margin-top:1px}
.env-strip .address{position:absolute;left:17px;top:54px;font-size:5px;line-height:1.3;letter-spacing:.03em}
.env-strip .vrule{position:absolute;left:85px;top:53px;width:1px;height:19px;background:var(--ink)}
.env-strip .contact{position:absolute;left:91px;top:53px;font-size:5px;line-height:1.3}

/* envelope back */
.env-back{left:632px;top:198px;width:343px;height:157px;background:var(--paper)}
.env-back .flap{position:absolute;left:0;top:0;width:343px;height:58px}
.env-back .lockup{position:absolute;left:122px;top:17px}
.env-back .brand{font-size:24px}
.env-back .brand-tag{font-size:5px;margin-top:1px}

/* envelope front */
.env-front{left:613px;top:301px;width:344px;height:157px;background:var(--paper)}
.env-front .header{height:54px;background:var(--red);position:relative}
.env-front .lockup{position:absolute;left:17px;top:18px}
.env-front .brand{font-size:19px}
.env-front .brand-tag{font-size:3.8px;margin-top:1px}
.env-front .address{position:absolute;left:17px;top:101px;font-size:5px;line-height:1.3;letter-spacing:.03em}
.env-front .contact{position:absolute;left:17px;top:117px;font-size:5px;line-height:1.3}

/* notepads */
.pad{width:129px;height:188px}
.pad .rings{position:absolute;left:6px;right:6px;top:0;height:6px;background:repeating-linear-gradient(90deg,#9a9a9a 0 1px,transparent 1px 8px)}
.pad-cover{left:1023px;top:77px;background:var(--ink)}
.pad-cover .lockup{position:absolute;left:28px;top:84px}
.pad-cover .brand{font-size:18px}
.pad-cover .brand-tag{font-size:3.5px;margin-top:1px}
.pad-cover .web{position:absolute;left:0;right:0;top:171px;text-align:center;color:var(--white);font-size:5px}
.pad-sheet{left:1025px;top:297px;background:var(--paper)}
.pad-sheet .lockup{position:absolute;left:40px;top:19px}
.pad-sheet .brand{font-size:12px}
.pad-sheet .brand-tag{font-size:2.6px;margin-top:1px}
.pad-sheet .lines{position:absolute;left:13px;right:12px;top:54px;height:107px;background:repeating-linear-gradient(180deg,transparent 0 10px,#cfc9ca 10px 10.6px)}
.pad-sheet .web{position:absolute;left:0;right:0;top:173px;text-align:center;font-size:5px;color:var(--grey)}

/* folder outside */
.folder-out{left:47px;top:560px;width:510px;height:321px;background:var(--white)}
.folder-out .back{position:absolute;left:0;top:0;width:254px;height:321px;background:var(--ink)}
.folder-out .back .lockup{position:absolute;left:53px;top:140px}
.folder-out .brand{font-size:40px}
.folder-out .brand-tag{font-size:8px;margin-top:2px}
.folder-out .back .address{position:absolute;left:0;right:0;top:250px;text-align:center;color:var(--white);font-size:5px;line-height:1.35;letter-spacing:.03em}
.folder-out .back .rule{position:absolute;left:113px;top:268px;width:28px;height:1px;background:var(--white)}
.folder-out .back .contact{position:absolute;left:0;right:0;top:276px;color:var(--white);font-size:5px;display:grid;grid-template-columns:auto auto;justify-content:center;column-gap:6px;row-gap:1px}
.folder-out .band{position:absolute;left:254px;top:126px;width:256px;height:63px;background:var(--red)}
.folder-out .band .lockup{position:absolute;left:37px;top:9px}

/* folder inside */
.folder-in{left:610px;top:562px;width:510px;height:322px;background:linear-gradient(90deg,#f4f4f4,#fff 60%,#e7e7e7 100%)}
.folder-in .spine{position:absolute;left:254px;top:0;width:2px;height:322px;background:linear-gradient(90deg,#cfcfcf,#f0f0f0)}
.folder-in .pockets{position:absolute;left:0;top:0;width:510px;height:322px}
.folder-in .lockup{position:absolute;top:236px}
.folder-in .lockup--left{left:60px}
.folder-in .lockup--right{left:323px}
.folder-in .brand{font-size:34px}
.folder-in .brand-tag{font-size:7px;margin-top:2px}
</style>
</head>
<body>

<svg width="0" height="0" style="position:absolute" aria-hidden="true">
  <defs>
    <symbol id="i-phone" viewBox="0 0 10 10"><path d="M2 0.5h2l1 2.5-1.3 1a6 6 0 0 0 2.3 2.3l1-1.3 2.5 1v2a1.5 1.5 0 0 1-1.5 1.5A8.5 8.5 0 0 1 0.5 2 1.5 1.5 0 0 1 2 0.5z"/></symbol>
    <symbol id="i-mobile" viewBox="0 0 10 10"><path d="M2.5 0h5v10h-5zM3.5 1v7h3V1z"/></symbol>
    <symbol id="i-mail" viewBox="0 0 10 10"><path d="M0 2h10v6H0zM1 3v.3l4 2.5 4-2.5V3z"/></symbol>
    <symbol id="i-globe" viewBox="0 0 10 10"><path d="M5 0a5 5 0 1 0 0 10A5 5 0 0 0 5 0zm0 1.5a3.5 3.5 0 1 1 0 7 3.5 3.5 0 0 1 0-7zM3 4h4v2H3z"/></symbol>
  </defs>
</svg>

<!-- business card front -->
<section class="piece card-front" aria-label="Business card front">
  <div class="lockup"><span class="brand brand--dark">Brenvik</span><span class="brand-tag">Tape and Packaging Specialists</span></div>
  <div class="divider"></div>
  <div class="holder">
    <p class="holder-name">ALDEN REYES</p>
    <p class="holder-role">President</p>
    <p class="address">4120 Cedar Row<br>Halton, Canada 52810</p>
    <ul class="contact">
      <li><svg class="icon icon--red"><use href="#i-phone"/></svg>612-555-0148</li>
      <li><svg class="icon icon--red"><use href="#i-mobile"/></svg>612-555-0193</li>
      <li><svg class="icon icon--red"><use href="#i-mail"/></svg>info@brenvik.com</li>
      <li><svg class="icon icon--red"><use href="#i-globe"/></svg>www.brenvik.com</li>
    </ul>
  </div>
</section>

<!-- business card back -->
<section class="piece card-back" aria-label="Business card back">
  <div class="mark"></div>
  <p class="web">www.brenvik.com</p>
</section>

<!-- letterhead -->
<section class="piece letterhead" aria-label="Letterhead">
  <header class="header">
    <div class="lockup"><span class="brand brand--light">Brenvik</span><span class="brand-tag">Tape and Packaging Specialists</span></div>
    <p class="header-address">4120 Cedar Row<br>Halton, Canada 52810<br>info@brenvik.com</p>
    <div class="header-rule"></div>
    <ul class="contact">
      <li><svg class="icon icon--white"><use href="#i-phone"/></svg>612-555-0148</li>
      <li><svg class="icon icon--white"><use href="#i-mobile"/></svg>612-555-0193</li>
      <li><svg class="icon icon--white"><use href="#i-globe"/></svg>www.brenvik.com</li>
    </ul>
  </header>
  <div class="letter-body">
    <p class="salutation">Dear Mr. Reyes,</p>
    <p>Lorem ipsum dolor sit amet, consectetur adipiscing elit. Donec orci purus, luctus vitae dignissim eu, iaculis sed purus. Vivamus faucibus, ipsum nec aliquet viverra, leo mauris condimentum ligula, sit amet sagittis enim ligula quis arcu. Nam egestas tortor id nisi porttitor mattis. In tortor ante, ultricies in suscipit a, tempus non massa. Vivamus et auctor mi. Fusce vel massa nulla. Phasellus nec eros mauris, et scelerisque orci.</p>
    <p>Donec malesuada orci vitae nulla accumsan porta a id massa. Quisque accumsan iaculis magna sit amet fringilla. Maecenas consequat, magna eget tincidunt semper, odio nibh rutrum mi, id feugiat ante nisi eu risus. Vestibulum nunc orci, rhoncus a placerat in, ultricies in mi. Cras mattis varius eros, vel fringilla nisi suscipit eget. Quisque scelerisque sagittis nulla at porttitor.</p>
    <p>Sed id augue vitae urna euismod commodo aliquet a quam. Pellentesque arcu velit, cursus et malesuada ut, consequat et diam. Nullam erat sem, rhoncus id ullamcorper vitae, rhoncus et arcu. In ultricies ultricies nulla, ut rutrum nisi iaculis at. Donec eu magna a metus ornare faucibus. Fusce aliquet faucibus ultricies. Morbi semper, est id tincidunt gravida, sem arcu adipiscing lacus, ac bibendum nulla leo eu purus. Quisque nec diam sed risus consectetur a accumsan quis quis nibh. Vestibulum id purus lorem.</p>
    <p>It is a long established fact that a reader will be distracted by the readable content of a page when looking at its layout. The point of using Lorem Ipsum is that it has a more-or-less normal distribution of letters, as opposed to using 'Content here, content here', making it look like readable English. Many desktop publishing packages</p>
    <p class="signoff">Sincerely,</p>
    <div class="signature-line"></div>
    <p class="signer">Alden Reyes</p>
    <p class="signer-role">CEO/ Founder</p>
  </div>
</section>

<!-- envelope strip -->
<section class="piece env-strip" aria-label="Envelope window strip">
  <div class="header">
    <div class="lockup"><span class="brand brand--light">Brenvik</span><span class="brand-tag" style="color:var(--white)">Tape and Packaging Specialists</span></div>
  </div>
  <p class="address">4120 Cedar Row<br>Halton, Canada 52810<br>info@brenvik.com</p>
  <div class="vrule"></div>
  <ul class="contact">
    <li><svg class="icon icon--red"><use href="#i-phone"/></svg>612-555-0148</li>
    <li><svg class="icon icon--red"><use href="#i-mobile"/></svg>612-555-0193</li>
    <li><svg class="icon icon--red"><use href="#i-globe"/></svg>www.brenvik.com</li>
  </ul>
</section>

<!-- envelope back -->
<section class="piece env-back" aria-label="Envelope back">
  <svg class="flap" viewBox="0 0 343 58" preserveAspectRatio="none" aria-hidden="true">
    <path d="M0 0H343L337 40Q334 58 316 58H27Q9 58 6 40Z" fill="var(--ink)"/>
  </svg>
  <div class="lockup"><span class="brand brand--light">Brenvik</span><span class="brand-tag" style="color:var(--white)">Tape and Packaging Specialists</span></div>
</section>

<!-- envelope front -->
<section class="piece env-front" aria-label="Envelope front">
  <div class="header">
    <div class="lockup"><span class="brand brand--light">Brenvik</span><span class="brand-tag" style="color:var(--white)">Tape and Packaging Specialists</span></div>
  </div>
  <p class="address">4120 Cedar Row<br>Halton, Canada 52810</p>
  <ul class="contact">
    <li><svg class="icon icon--red"><use href="#i-phone"/></svg>612-555-0148</li>
    <li><svg class="icon icon--red"><use href="#i-mobile"/></svg>612-555-0193</li>
    <li><svg class="icon icon--red"><use href="#i-mail"/></svg>info@brenvik.com</li>
    <li><svg class="icon icon--red"><use href="#i-globe"/></svg>www.brenvik.com</li>
  </ul>
</section>

<!-- notepad cover -->
<section class="piece pad pad-cover" aria-label="Notepad cover">
  <div class="rings"></div>
  <div class="lockup"><span class="brand brand--light">Brenvik</span><span class="brand-tag" style="color:var(--white)">Tape and Packaging Specialists</span></div>
  <p class="web">www.brenvik.com</p>
</section>

<!-- notepad sheet -->
<section class="piece pad pad-sheet" aria-label="Notepad sheet">
  <div class="rings"></div>
  <div class="lockup"><span class="brand brand--dark">Brenvik</span><span class="brand-tag">Tape and Packaging Specialists</span></div>
  <div class="lines"></div>
  <p class="web">www.brenvik.com</p>
</section>

<!-- folder outside -->
<section class="piece folder-out" aria-label="Presentation folder outside">
  <div class="back">
    <div class="lockup"><span class="brand brand--light">Brenvik</span><span class="brand-tag" style="color:var(--white)">Tape and Packaging Specialists</span></div>
    <p class="address">4120 Cedar Row<br>Halton, Canada 52810</p>
    <div class="rule"></div>
    <ul class="contact">
      <li><svg class="icon icon--white"><use href="#i-phone"/></svg>612-555-0148</li>
      <li><svg class="icon icon--white"><use href="#i-mobile"/></svg>612-555-0193</li>
      <li><svg class="icon icon--white"><use href="#i-mail"/></svg>info@brenvik.com</li>
      <li><svg class="icon icon--white"><use href="#i-globe"/></svg>www.brenvik.com</li>
    </ul>
  </div>
  <div class="band">
    <div class="lockup"><span class="brand brand--light">Brenvik</span><span class="brand-tag" style="color:var(--white)">Tape and Packaging Specialists</span></div>
  </div>
</section>

<!-- folder inside -->
<section class="piece folder-in" aria-label="Presentation folder inside">
  <div class="spine"></div>
  <svg class="pockets" viewBox="0 0 510 322" aria-hidden="true">
    <path d="M0 192H226Q238 192 241 206L255 322H0Z" fill="var(--ink)"/>
    <path d="M510 192H284Q272 192 269 206L255 322H510Z" fill="var(--ink)"/>
  </svg>
  <div class="lockup lockup--left"><span class="brand brand--light">Brenvik</span><span class="brand-tag" style="color:var(--white)">Tape and Packaging Specialists</span></div>
  <div class="lockup lockup--right"><span class="brand brand--light">Brenvik</span><span class="brand-tag" style="color:var(--white)">Tape and Packaging Specialists</span></div>
</section>

</body>
</html>
```